Business card for Northland's Blue Wagon.

Good day i am looking for a business card design for my business.
The name of the business is Northland's Blue Wagon. It is a van rental business that provides a driver and helper to the customer. Customer have use to van for small moves, studio or 1 bedroom, Moving furniture like couch or kitchen cabinets.
We are available evenings, weekends and holidays.
the means to contact us is by phone at 628-947-2071; By emails at Oakridge@northlandsbluewagon.net; or by social media, Facebook and Instagram.
You can see attached pictures of the van and or logo.

```html
<!DOCTYPE html>
<html lang="en">
<head>
<meta charset="utf-8">
<title>Northland's Blue Wagon – Business Card</title>
<link rel="stylesheet" href="https://fonts.googleapis.com/css2?family=Arimo:wght@400;700&display=swap">
<style>
  :root {
    --brand-red: #d40000;
    --ink: #1a1a1a;
    --muted: #777777;
    --rule: #cfcfcf;
    --paper: #ffffff;
    --backdrop: #2b2b2b;
  }
  * { box-sizing: border-box; margin: 0; padding: 0; }
  html, body { width: 1200px; height: 874px; overflow: hidden; }
  body {
    background: var(--backdrop);
    font-family: "Arimo", Arial, sans-serif;
    position: relative;
  }
  .card {
    position: absolute;
    left: 320px;
    width: 560px;
    height: 320px;
    border-radius: 18px;
    overflow: hidden;
  }
  .card-back { top: 77px; background: var(--brand-red); }
  .card-front { top: 477px; background: var(--paper); }

  /* back side */
  .back-mark {
    position: absolute; left: 0; right: 0; top: 92px;
    display: flex; align-items: center; justify-content: center; gap: 14px;
    color: var(--paper); font-weight: 700; font-size: 30px;
  }
  .mark-dot { width: 22px; height: 22px; border-radius: 50%; background: currentColor; flex: none; }
  .back-url {
    position: absolute; left: 0; right: 0; top: 238px;
    text-align: center; color: var(--paper); font-size: 17px;
  }

  /* front side */
  .front-mark {
    position: absolute; right: 40px; top: 50px; width: 210px;
    display: flex; flex-direction: column; align-items: center; gap: 10px;
    color: var(--brand-red); font-weight: 700; font-size: 19px; line-height: 1.2; text-align: center;
  }
  .person { position: absolute; left: 42px; top: 112px; }
  .person-name { color: var(--brand-red); font-weight: 700; font-size: 28px; line-height: 1; }
  .person-title { color: var(--muted); font-size: 15px; margin-top: 4px; }
  .divider { position: absolute; height: 1px; background: var(--rule); }
  .divider-main { left: 42px; width: 290px; top: 166px; }
  .divider-social { left: 370px; right: 40px; top: 212px; }
  .contact-list { position: absolute; left: 42px; top: 176px; list-style: none; }
  .contact-list li {
    display: flex; align-items: center; gap: 9px;
    color: #333; font-size: 14px; line-height: 22px;
  }
  .contact-list svg { width: 13px; height: 13px; fill: var(--brand-red); flex: none; }
  .social {
    position: absolute; right: 40px; top: 220px;
    display: flex; flex-direction: column; align-items: flex-end; gap: 4px;
    color: #444; font-size: 14px;
  }
  .social-dot { width: 16px; height: 16px; border-radius: 50%; background: var(--brand-red); margin-right: 34px; }
  .footer-stripe { position: absolute; left: 0; right: 0; top: 278px; height: 3px; background: var(--ink); }
  .footer-band { position: absolute; left: 0; right: 0; top: 285px; bottom: 0; background: var(--brand-red); }
</style>
</head>
<body>
  <section class="card card-back" aria-label="Card back">
    <div class="back-mark"><span class="mark-dot"></span><span>Northland's Blue Wagon</span></div>
    <p class="back-url">www.northlandsbluewagon.net</p>
  </section>

  <section class="card card-front" aria-label="Card front">
    <div class="front-mark"><span class="mark-dot"></span><span>Northland's<br>Blue Wagon</span></div>

    <div class="person">
      <h1 class="person-name">Mark Ellison</h1>
      <p class="person-title">President</p>
    </div>
    <div class="divider divider-main"></div>

    <ul class="contact-list">
      <li>
        <svg viewBox="0 0 24 24" aria-hidden="true"><path d="M6.6 10.8a15.1 15.1 0 0 0 6.6 6.6l2.2-2.2a1 1 0 0 1 1-.25 11.4 11.4 0 0 0 3.6.6 1 1 0 0 1 1 1V20a1 1 0 0 1-1 1A17 17 0 0 1 3 4a1 1 0 0 1 1-1h3.5a1 1 0 0 1 1 1c0 1.25.2 2.45.6 3.6a1 1 0 0 1-.25 1z"/></svg>
        628-947-2071
      </li>
      <li>
        <svg viewBox="0 0 24 24" aria-hidden="true"><path d="M2 5h20v14H2z M2 5l10 8 10-8" /></svg>
        Oakridge@northlandsbluewagon.net
      </li>
      <li>
        <svg viewBox="0 0 24 24" aria-hidden="true"><circle cx="12" cy="12" r="10"/></svg>
        www.northlandsbluewagon.net
      </li>
    </ul>

    <div class="divider divider-social"></div>
    <div class="social"><span class="social-dot"></span><span>northlandsbluewagon</span></div>

    <div class="footer-stripe"></div>
    <div class="footer-band"></div>
  </section>
</body>
</html>
```